Social responsible Renewable Energy company

We at voltaQ are an independent power producer company founded in 2021 that handles large scale deployment of Renewable Energy and carbon neutral Energy as a service model. We offer turnkey solutions using solar panel systems and this could be incorporated in our business cards. You can also find our logo in the documents provided. Another key issue is that the business cards will be printed on recicled paper, not sure if this is a limitation in deciding the design. The recycled sign should also be added on the business card and stating that the paper used was recycled. Our website is www.myvoltaq.example. It should also be very professional, not too dreamy but still needs to capture your imagination. We are really excited to get your ideas !

Target Market(s)

Renewable Energy market

Contact Information for Business Card

The business card will be printed on recycled paper. Name of the company is voltaQ. Website is www.myvoltaq.example

Requirements
Nice to have
• Our motto: Powered by renewable, driven by people.

```html
<!DOCTYPE html>
<html lang="en">
<head>
<meta charset="utf-8">
<title>voltaQ business card</title>
<link rel="stylesheet" href="https://fonts.googleapis.com/css2?family=Open+Sans:wght@400;600;700&display=swap">
<style>
  :root {
    --bg: #ebebeb;
    --kraft: #bba88c;
    --kraft-deep: #ad997c;
    --ink: #3a3a3c;
    --ink-soft: #4a4a4c;
    --rule: #56524c;
  }
  * { margin: 0; padding: 0; box-sizing: border-box; }
  html, body { width: 1200px; height: 801px; overflow: hidden; }
  body {
    background: var(--bg);
    font-family: "Open Sans", sans-serif;
    color: var(--ink);
    position: relative;
  }
  .card {
    position: absolute;
    top: 246px;
    width: 540px;
    height: 309px;
    background: var(--kraft);
    border-radius: 3px;
  }
  .card--front { left: 40px; }
  .card--back { left: 620px; }

  .brand-name {
    position: absolute;
    top: 24px;
    right: 110px;
    font-size: 54px;
    font-weight: 700;
    letter-spacing: -1px;
    color: var(--ink);
    line-height: 1;
  }
  .cert-badge {
    position: absolute;
    top: 26px;
    right: 30px;
    width: 52px;
    height: 52px;
    border: 2px solid var(--ink-soft);
    border-radius: 50%;
  }
  .recycled-note {
    position: absolute;
    top: 84px;
    right: 24px;
    font-size: 9px;
    color: var(--ink-soft);
  }
  .rule {
    position: absolute;
    height: 1px;
    background: var(--rule);
  }
  .rule--top { top: 104px; left: 30px; right: 24px; }
  .rule--mid { top: 226px; left: 30px; width: 230px; }

  .address {
    position: absolute;
    top: 114px;
    right: 24px;
    text-align: right;
    font-size: 14px;
    line-height: 1.35;
    color: var(--ink-soft);
  }
  .person {
    position: absolute;
    left: 30px;
    top: 178px;
  }
  .person-name {
    font-size: 19px;
    font-weight: 700;
    letter-spacing: 0.3px;
    text-transform: uppercase;
    line-height: 1.1;
  }
  .person-role { font-size: 14px; color: var(--ink-soft); }

  .contacts {
    position: absolute;
    left: 30px;
    top: 236px;
    list-style: none;
    font-size: 14px;
    line-height: 21px;
    color: var(--ink-soft);
  }
  .contacts li { display: flex; align-items: center; gap: 8px; }
  .contacts svg { width: 11px; height: 11px; fill: var(--ink-soft); }

  .back-mark {
    position: absolute;
    top: 96px;
    left: 0;
    right: 0;
    text-align: center;
    font-size: 48px;
    font-weight: 700;
    color: var(--kraft-deep);
  }
  .motto {
    position: absolute;
    bottom: 42px;
    left: 0;
    right: 0;
    text-align: center;
    font-size: 15px;
    color: var(--ink-soft);
  }
</style>
</head>
<body>
  <section class="card card--front">
    <div class="brand-name">voltaQ</div>
    <div class="cert-badge" aria-label="certification badge"></div>
    <div class="recycled-note">Printed on recycled paper</div>
    <div class="rule rule--top"></div>
    <address class="address">1180 Harbor Crest Way<br>Seabrook CA 90210</address>
    <div class="person">
      <div class="person-name">Leo Marren</div>
      <div class="person-role">President</div>
    </div>
    <div class="rule rule--mid"></div>
    <ul class="contacts">
      <li>
        <svg viewBox="0 0 24 24"><path d="M6.6 10.8a15.1 15.1 0 0 0 6.6 6.6l2.2-2.2a1 1 0 0 1 1-.25 11.4 11.4 0 0 0 3.6.57 1 1 0 0 1 1 1V20a1 1 0 0 1-1 1A17 17 0 0 1 3 4a1 1 0 0 1 1-1h3.5a1 1 0 0 1 1 1c0 1.25.2 2.45.57 3.57a1 1 0 0 1-.25 1z"/></svg>
        555-014-2870
      </li>
      <li>
        <svg viewBox="0 0 24 24"><path d="M2 5h20v14H2zM2 5l10 8 10-8v3l-10 8L2 8z"/></svg>
        lmarren@myvoltaq.example
      </li>
      <li>
        <svg viewBox="0 0 24 24"><circle cx="12" cy="12" r="10"/></svg>
        www.myvoltaq.example
      </li>
    </ul>
  </section>

  <section class="card card--back">
    <div class="back-mark">voltaQ</div>
    <p class="motto">Powered by renewable, driven by people.</p>
  </section>
</body>
</html>
```